Design a menu for health restaurant

A health food restaurant in Los Angeles is seeking menu design. Our foods are made from scratch using whole ingredients.
Name: Grove Pantry
Address: 1000 E 60th StLos Angeles, CA 90347
Website: www.GrovePantry-example.com
We are looking for a clean and simple menu. Brand colors are white/tan, green and orange.

Please see attached excel with menu items and logo. We do not yet have prices.

Colors
f78f20
9bcb3c
ffffff
fff3d1

Requirements
Must have
• Easy to read.
Trifold menu design (front and back).
VEGAN, VEGETARIAN, GLUTEN FREE, CONTAINS NUTS symbols.
Logo.
Nice to have
• Incorporate brand colors, but still be easy to read.
We would like to use the Belco font (attached) if it works. If not we are open to a similar font that is easy to read.

Please see attached images.
We like the images and headers of OPTION 1. Would like something similar in trifold format.
We like the clean fonts of OPTION 2.

```html
<!DOCTYPE html>
<html lang="en">
<head>
<meta charset="utf-8">
<title>Grove Pantry — Trifold Menu</title>
<link rel="stylesheet" href="https://fonts.googleapis.com/css2?family=Josefin+Sans:wght@400&family=Open+Sans:wght@400&display=swap">
<style>
:root{
  --orange:#f78f20;
  --green:#9bcb3c;
  --white:#ffffff;
  --tan:#fed7a3;
  --ink:#1a1a1a;
  --photo-warm:#e9c7a0;
  --photo-green:#a9c27e;
  --photo-gold:#f2c14a;
  --photo-pink:#f07a86;
}
*{margin:0;padding:0;box-sizing:border-box}
html,body{width:1200px;height:640px;overflow:hidden;background:var(--tan)}
.canvas{position:relative;width:1200px;height:640px}
.sheet{position:absolute;top:148px;width:510px;height:384px;background:var(--white)}
.sheet--front{left:68px}
.sheet--back{left:624px}

.col{position:absolute;top:8px;height:370px;display:flex;flex-direction:column;justify-content:space-between}

.band{flex:none;height:17px;width:134px;white-space:nowrap;font-family:"Josefin Sans",sans-serif;font-size:15px;line-height:20px;letter-spacing:.5px;color:var(--ink);padding-left:20px;text-transform:uppercase;margin-bottom:4px}
.band--orange{background:var(--orange)}
.band--green{background:var(--green)}
.band--center{padding-left:0;text-align:center}
.band--small{font-size:11px;line-height:19px;padding-left:8px;letter-spacing:.3px}

.item h3{font-family:"Josefin Sans",sans-serif;font-weight:400;font-size:8.6px;line-height:9.4px;text-transform:uppercase;color:var(--ink)}
.item p{font-family:"Open Sans",sans-serif;font-size:4.8px;line-height:5.6px;color:var(--ink);margin-top:1px}
.item--right{text-align:right}

.row{display:flex;gap:5px;align-items:flex-start}
.row > .item,.row > .stack{flex:1;min-width:0}
.stack{display:flex;flex-direction:column;gap:5px}

.photo{flex:none;border-radius:2px}
.photo--pastry{background:radial-gradient(circle at 50% 55%,#e6a95a,var(--photo-warm) 70%,#fff)}
.photo--toast{background:radial-gradient(circle,#d86a5a,#c7d89a 60%,#f4f4f4)}
.photo--smoothie{background:linear-gradient(180deg,#f7f7f7,var(--photo-gold) 40%,#f6d36c)}
.photo--bowl{background:radial-gradient(circle,#b8c980,#e0d0b0 70%,#f4f4f4)}
.photo--salad{background:radial-gradient(circle,#d65b4b,var(--photo-green) 60%,#f5f5f5)}
.photo--soup{background:radial-gradient(circle,#f0a43a,#f4d9a8 65%,#fafafa)}
.photo--burger{background:radial-gradient(circle,#8a5a3a,#9dbb6a 60%,#f4f4f4)}
.photo--chips{background:radial-gradient(circle,#c6d88a,#f1f1f1 70%)}
.photo--drink{background:radial-gradient(circle at 50% 60%,var(--photo-pink),#fbe3e3 75%)}

.brand{flex:none;height:60px;display:flex;align-items:center;justify-content:center;gap:5px}
.brand span{font-family:"Josefin Sans",sans-serif;font-size:11px;color:var(--orange);text-transform:uppercase;letter-spacing:.5px}
</style>
</head>
<body>
<div class="canvas">

  <section class="sheet sheet--front">
    <div class="col" style="left:16px;width:142px">
      <div class="band band--orange">Breakfast</div>
      <div class="row">
        <div class="item"><h3>Pastries</h3><p>Croissant (regular, almond, chocolate)<br>Blueberry Muffin<br>Superseed Cookie</p></div>
        <div class="photo photo--pastry" role="img" aria-label="Photo of croissants" style="width:38px;height:42px"></div>
      </div>
      <div class="item"><h3>Parfait</h3><p>Fresh strawberries and blueberries on yogurt and muesli and topped with honey drizzle</p></div>
      <div class="item"><h3>Avocado Super Toast</h3><p>Avocado Mash, Tomato, Basil, Ground Flax, Hemp Seed, Chickpeas, and Moringa Powder on Whole Wheat Bread</p></div>
      <div class="photo photo--toast" role="img" aria-label="Photo of avocado toast" style="width:50px;height:40px"></div>
      <div class="item"><h3>Brunch Burger</h3><p>House seasoned beef burger topped with an over medium egg, red leaf lettuce, tomato, housemade pickles and Grove Sauce on a bun</p></div>
      <div class="item"><h3>Breakfast Sammy</h3><p>Your choice of over medium egg or tofu steak with guacamole, tomato, and Grove Sauce on an English muffin</p></div>
      <div class="item"><h3>AM Burrito</h3><p>Scrambled eggs, onion, red bell pepper, black beans, house made salsa, yogurt, and pepper jack cheese in a tortilla</p></div>
      <div class="band band--green" style="margin-top:6px">Smoothies</div>
      <div class="item"><h3>Green Machine Smoothie</h3><p>Romaine, spinach, banana, mango, pineapple, flaxmilk, spirulina, almond butter</p></div>
      <div class="item"><h3>Acai Smoothie</h3><p>Acai, blueberries, banana, pineapple, Macqui berry, flaxmilk, almond butter</p></div>
    </div>

    <div class="col" style="left:186px;width:148px">
      <div class="brand">
        <svg width="14" height="14" viewBox="0 0 14 14" aria-hidden="true"><circle cx="7" cy="7" r="6" fill="none" stroke="var(--orange)" stroke-width="1.5"/></svg>
        <span>Grove Pantry</span>
      </div>
      <div class="row" style="align-items:center">
        <div class="item item--right"><h3>Mango Smoothie</h3><p>Mango, flaxmilk, banan, hemp seeds</p></div>
        <div class="photo photo--smoothie" role="img" aria-label="Photo of mango smoothie" style="width:58px;height:44px"></div>
      </div>
      <div class="band band--orange band--center" style="margin-top:4px">Bowls</div>
      <div class="row">
        <div class="item"><h3>Southwest Bowl</h3><p>Your choice of protein with corn, black beans, red onions, almonds and avocado over quinoa with lime hot sauce</p></div>
        <div class="photo photo--bowl" role="img" aria-label="Photo of southwest bowl" style="width:56px;height:40px"></div>
      </div>
      <div class="item"><h3>Chimi Bowl</h3><p>Your choice of protein with red bell pepper, mushrooms, zucchini, squash, onion, cherry tomatoes and fresh herb chimichurri on wild and brown rice</p></div>
      <div class="item"><h3>Soba Noodle Bowl</h3><p>Your choice of protein with spinach, snow peas, roasted carrots, red bell pepper, cilantro, sesame seeds and ginger lime sauce over soba noodles</p></div>
      <div class="row">
        <div class="photo photo--salad" role="img" aria-label="Photo of hollywood bowl" style="width:56px;height:42px"></div>
        <div class="item item--right"><h3>Hollywood Bowl</h3><p>Your choice of protein with broccoli, roasted corn, cherry tomatoes, basil, pepitas, flax seeds and lemon juice on wild and brown rice</p></div>
      </div>
      <div class="item"><h3>Grove Bowl</h3><p>Your choice of protein with roasted chickpeas and cauliflower, zesty fennel salad and citrus yogurt</p></div>
    </div>

    <div class="col" style="left:352px;width:146px">
      <div class="item"><h3>Buddha Bowl</h3><p>Your choice of protein with corn, red kale, sweet potatoes, red cabbage, parsley, oregano, hummus, and farro</p></div>
      <div class="item"><h3>Chili Rice Bowl</h3><p>Chicken, onions, bell peppers, jalapeños, black &amp; kidney beans, and tomato over brown rice</p></div>
      <div class="band band--green band--center" style="margin-top:4px">Soups</div>
      <div class="row">
        <div class="item"><h3>Chicken Noodle</h3><p>Chicken, egg noodles, root vegetables, oregano &amp; peppercorns</p></div>
        <div class="photo photo--soup" role="img" aria-label="Photo of butternut squash soup" style="width:56px;height:38px"></div>
      </div>
      <div class="item"><h3>Grove Chili</h3><p>Chicken, onions, bell peppers, jalapeños, black &amp; kidney beans, and tomato</p></div>
      <div class="item"><h3>Seasonal Rotating<br>(Butternut Squash Soup V+, GF)</h3><p>Butternut squash blended with warm spices, and coconut milk</p></div>
      <div class="band band--orange band--center" style="margin-top:4px">Wraps</div>
      <div class="item"><h3>Rancher's Wrap</h3><p>Tomato, red onion, hard boiled egg, avocado, feta cheese, microgreens, romaine, grilled chicken and Ranch dressing in a grilled wrap</p></div>
      <div class="item"><h3>Vegan Tuna Wrap</h3><p>Vegan tuna, romaine, avocado, celery, shallot, and oregano with Herbalicious Sauce in a whole grain wrap</p></div>
      <div class="item"><h3>Vegetarian Wrap</h3><p>Roasted chickpeas, romaine, avocado, red bell pepper, shaved carrots, cucumber, spinach, basil, black beans and feta with lemon-hummus in a sprouted 7-grain wrap</p></div>
    </div>
  </section>

  <section class="sheet sheet--back">
    <div class="col" style="left:16px;width:142px">
      <div class="band band--green band--center">Salad</div>
      <div class="item"><h3>Avocado, Golden Beet,<br>and Cranberry Salad</h3><p>Gold beets, avocado, dried cranberries, watermelon radish, red kale, romaine, mixed greens, and pepitas served with Golden Buddha dressing</p></div>
      <div class="item"><h3>Burrata Salad</h3><p>Tomato, melon, shredded basil, balsamic glaze, fresh cracked pepper, and olive oil with burrata</p></div>
      <div class="row">
        <div class="item"><h3>Mediterranean Salad</h3><p>Cucumbers, Kalamata olives, cherry tomatoes, parsley, tricolor quinoa, hard-boiled egg, and hummus on mixed greens, romaine, and red cabbage with lemon-olive oil dressing</p></div>
        <div class="photo photo--salad" role="img" aria-label="Photo of mediterranean salad" style="width:54px;height:42px;margin-top:8px"></div>
      </div>
      <div class="row">
        <div class="item item--right"><h3>Vegan Chef Salad</h3><p>Roasted potatoes and carrots, chickpeas, avocado, microgreens and walnuts on mixed greens, romaine, and red kale with vegan ranch.</p></div>
        <div class="photo photo--salad" role="img" aria-label="Photo of vegan chef salad" style="width:54px;height:40px"></div>
      </div>
      <div class="item"><h3>Rancher's Salad</h3><p>Tomato, red onion, hard boiled egg, avocado, feta cheese, microgreens, and grilled chicken on romaine with Ranch dressing.</p></div>
      <div class="band band--orange band--small" style="margin-top:4px">Burgers N' Sammies</div>
      <div class="item"><h3>Air Fried Chicken Sammy</h3><p>Air fried chicken breast topped with red leaf lettuce, tomato, house made pickles and Grove Sauce on a bun served with choice of salad of fries</p></div>
      <div class="item"><h3>Grilled Chicken Sammy</h3><p>Grilled chicken topped with guacamole, red leaf lettuce, tomato, house made pickles and Grove Sauce. Served with regular fries or side salad</p></div>
    </div>

    <div class="col" style="left:178px;width:150px;height:350px">
      <div class="item"><h3>Classic Beef Burger</h3><p>House seasoned beef burger topped with red leaf lettuce, tomato, cheddar cheese, house made pickles and Grove Sauce on a bun served with choice of salad of fries</p></div>
      <div class="item"><h3>Black Bean Pine Nut Burger</h3><p>House made black bean pine nut burger topped with red leaf lettuce, tomato, house made pickles and mustard aioli on a bun served with choice of salad of fries</p></div>
      <div class="row">
        <div class="photo photo--burger" role="img" aria-label="Photo of salmon burger" style="width:70px;height:50px"></div>
        <div class="item item--right"><h3>Salmon Burger</h3><p>House made salmon burger topped with red leaf lettuce, tomato, house made pickles and Grove yogurt on a bun served with choice of salad of fries</p></div>
      </div>
      <div class="band band--green band--small" style="margin-top:4px;padding-left:10px">Snacks N' Sides</div>
      <div class="item"><h3>Fries</h3><p>Hand cut air-fries with house seasonings. Choose regular or sweet potato fries</p></div>
      <div class="row">
        <div class="stack">
          <div class="item"><h3>Side Salad</h3><p>Your choice of House, Golden Beet, Mediterranean, or Vegan Chef side salad. (24oz)</p></div>
          <div class="item"><h3>Guac + Chips</h3><p>Guacamole with blue corn tortilla chips</p></div>
          <div class="item"><h3>Hummus + Chips</h3><p>Hummus with blue corn tortilla chips</p></div>
        </div>
        <div class="photo photo--chips" role="img" aria-label="Photo of guacamole and chips" style="width:44px;height:40px;margin-top:6px"></div>
      </div>
      <div class="band band--orange band--center" style="margin-top:4px">Combos</div>
      <div class="item"><h3>Soup + Salad</h3><p>Your choice of soup and side salad. 16oz soup + 38oz salad</p></div>
      <div class="item"><h3>Avo Toast Combo</h3><p>Half avocado toast and your choice of soup. 16oz</p></div>
      <div class="item"><h3>Soup + Sammy</h3><p>Your choice of soup and sandwich. 16oz soup + Sandwich</p></div>
    </div>

    <div class="col" style="left:354px;width:146px">
      <div class="band band--green band--center">Desserts</div>
      <div class="item"><h3>Date Coffee Cake</h3><p>Signature date coffee cake with walnuts</p></div>
      <div class="item"><h3>Fruit + Spices</h3><p>Strawberry, pineapple, green apple, orange, and blueberries with lime and chili seasoning</p></div>
      <div class="item"><h3>Cookies</h3><p>Your choice of Chocolate Chip or Double Chocolate Chip fresh baked cookie</p></div>
      <div class="item"><h3>Grove Chocolate Mousse</h3><p>Served with grated dark chocolate</p></div>
      <div class="band band--orange band--center" style="margin-top:4px">Drinks</div>
      <div class="item"><h3>Coffee</h3><p>We proudly serve Ridgeline Coffee, a local roaster</p></div>
      <div class="item"><h3>Power Date Shake</h3><p>Ice-blended energy smoothie featuring dates and coffee</p></div>
      <div class="item"><h3>Heart Beet Juice</h3><p>Red beet, apple, carrot, ginger, parsley, and lemon</p></div>
      <div class="item"><h3>Green Leafy Juice</h3><p>Spinach, kale, cucumber, apple, and oranges</p></div>
      <div class="item"><h3>Orange Turmeric Juice</h3><p>Turmeric, ginger, lemon, carrot, and orange topped with cracked black pepper</p></div>
      <div class="item"><h3>Fireshot</h3><p>Ginger and lemon shot topped with cayenne</p></div>
      <div class="item"><h3>Lemonade</h3><p>House Made Lemonade. Choice of unsweetened or agave sweetened in Regular, Raspberry, and Lavender flavors</p></div>
      <div class="row" style="align-items:center">
        <div class="item"><h3>Tea</h3><p>Hot or iced</p></div>
        <div class="photo photo--drink" role="img" aria-label="Photo of raspberry lemonade" style="width:36px;height:30px"></div>
      </div>
      <div class="item"><h3>Bottled Drinks</h3><p>Tidewell kombucha (Tidewell Trilogy, Tidewell Gingerberry, Tidewell Mango)<br>Brightfizz (Orange Mango, Lemon, Grapefruit)<br>Palmwell Coconut Original<br>Sparkling Water (Clearsprig)<br>Still Water (Clearsprig)</p></div>
    </div>
  </section>

</div>
</body>
</html>
```